Talvoro Equity LLC

Need Professional Business cards for New Investment Fund

Target Market(s)

High Quality investors

Industry/Entity Type

Financial

Contact Information for Business Card

Phone Number +1 555 284 6190
Name Milan Dorovsky
Title Fund Manager
email md@FundTalvoro.com
Website www.FundTalvoro.com

Colors

Designer to choose colors to be used in the design.

Requirements
Must have
• Must have our Logo and all of the above. Must be made so lettering and loge can be raised

```html
<!DOCTYPE html>
<html lang="en">
<head>
<meta charset="utf-8">
<title>Talvoro Equity — Business Card</title>
<link href="https://fonts.googleapis.com/css2?family=Source+Sans+3:wght@400;600;700&display=swap" rel="stylesheet">
<style>
  :root {
    --bg: #2c2d2f;
    --card-white: #ffffff;
    --card-shade: #eeeeee;
    --panel-dark: #3f4a3f;
    --brand-green: #1fd40f;
    --brand-green-deep: #14a80a;
    --text-light: #e6e9e6;
    --text-muted: #c9cfc9;
    --ink-dark: #3f4a3f;
  }
  * { box-sizing: border-box; margin: 0; padding: 0; }
  html, body { width: 1200px; height: 1000px; overflow: hidden; }
  body {
    background: var(--bg);
    font-family: "Source Sans 3", "Helvetica Neue", Arial, sans-serif;
    position: relative;
  }
  .card {
    position: absolute;
    left: 250px;
    width: 700px;
    height: 400px;
    overflow: hidden;
    box-shadow: 0 14px 30px rgba(0,0,0,0.45);
  }
  .card--back {
    top: 50px;
    background: linear-gradient(180deg, var(--card-white), var(--card-shade));
    display: flex;
    align-items: center;
    justify-content: center;
  }
  .card--front {
    top: 530px;
    background: linear-gradient(180deg, var(--card-white), var(--card-shade));
  }
  .wordmark {
    display: flex;
    align-items: center;
    gap: 14px;
    color: var(--ink-dark);
    font-weight: 700;
    letter-spacing: 2px;
    text-transform: uppercase;
  }
  .wordmark__square {
    width: 22px; height: 22px;
    background: var(--brand-green);
  }
  .card--back .wordmark { font-size: 34px; }
  .contact-panel {
    position: absolute;
    left: 0; top: 0;
    width: 290px; height: 100%;
    background: var(--panel-dark);
    padding: 92px 0 0 34px;
  }
  .contact-panel__name {
    color: var(--brand-green);
    font-weight: 700;
    font-size: 21px;
    letter-spacing: 1px;
    text-transform: uppercase;
  }
  .contact-panel__title {
    color: var(--text-light);
    font-weight: 600;
    font-size: 15px;
    margin-bottom: 20px;
  }
  .contact-list { list-style: none; }
  .contact-list li {
    display: flex;
    align-items: center;
    gap: 10px;
    color: var(--text-muted);
    font-size: 15px;
    line-height: 24px;
  }
  .contact-list svg { width: 13px; height: 13px; fill: var(--brand-green); flex: none; }
  .divider-band {
    position: absolute;
    left: 290px; top: 0;
    width: 20px; height: 100%;
    background: var(--card-white);
    border-left: 4px solid var(--card-white);
  }
  .divider-band::after {
    content: ""; position: absolute; left: 0; top: 0;
    width: 12px; height: 100%; background: var(--brand-green);
  }
  .edge-bands {
    position: absolute;
    right: 0; top: 0;
    width: 46px; height: 100%;
    display: flex; gap: 4px;
  }
  .edge-bands__dark { width: 18px; background: var(--ink-dark); }
  .edge-bands__green { flex: 1; background: linear-gradient(180deg, var(--brand-green), var(--brand-green-deep)); }
  .front-mark {
    position: absolute;
    left: 310px; right: 46px; top: 0; bottom: 0;
    display: flex; align-items: center; justify-content: center;
  }
  .front-mark .wordmark { font-size: 28px; }
</style>
</head>
<body>
  <section class="card card--back">
    <div class="wordmark"><span class="wordmark__square"></span>Talvoro Equity</div>
  </section>

  <section class="card card--front">
    <div class="contact-panel">
      <h1 class="contact-panel__name">Milan Dorovsky</h1>
      <p class="contact-panel__title">Fund Manager</p>
      <ul class="contact-list">
        <li><svg viewBox="0 0 16 16"><path d="M3 1h3l1 4-2 1a9 9 0 0 0 5 5l1-2 4 1v3a2 2 0 0 1-2 2A13 13 0 0 1 1 3a2 2 0 0 1 2-2z"/></svg>+1 555 284 6190</li>
        <li><svg viewBox="0 0 16 16"><path d="M1 3h14v10H1z M1 3l7 6 7-6" stroke="#3f4a3f" stroke-width="1.2"/></svg>md@FundTalvoro.com</li>
        <li><svg viewBox="0 0 16 16"><circle cx="8" cy="8" r="7"/></svg>www.FundTalvoro.com</li>
      </ul>
    </div>
    <div class="divider-band"></div>
    <div class="front-mark">
      <div class="wordmark"><span class="wordmark__square"></span>Talvoro Equity</div>
    </div>
    <div class="edge-bands"><span class="edge-bands__dark"></span><span class="edge-bands__green"></span></div>
  </section>
</body>
</html>
```